Business Card Design Project

I am looking for a business card design for my custom Audio/Video & Contracting business named Brelvora Systems Inc. We do not currently have a corporate logo so you should not feel constrained to work around an existing design. Your design should be elegant and clean while artistically conveying that we are a technology company. We provide A/V services for the commercial and residential markets and contracting services for residential remodeling and home theater construction. We do not have a particular color that we are looking to design around so feel free to be creative.

To get references of the kind of work that we do and design inspiration please visit the following sites:

http://www.quenlamark.us
www.morvethpro.com
www.feltonbraxa.com

Reason: I think we are getting close on a couple of the designs and want to give additional time to get tweaks done and to resubmit your designs.

Target Market(s)

Most of our clients are very wealthy and have been exposed to premium brand names in every aspect of their lives, (ie. - luxury autos, estate sized homes, fine jewelery and clothes) and your design needs to convey that same level of excellent design that they are used to.

Industry/Entity Type

Residential

Requirements
Should not have
• An extensive use of the color RED.

```html
<!DOCTYPE html>
<html lang="en">
<head>
<meta charset="utf-8">
<title>Brelvora Systems Inc. – Business Card</title>
<link rel="stylesheet" href="https://fonts.googleapis.com/css2?family=Source+Sans+3:wght@400&display=swap">
<style>
  :root {
    --page-bg: #e9e7e3;
    --card-white: #ffffff;
    --blue-deep: #0b4aa2;
    --blue-bright: #2a8ad6;
    --ink-blue: #1d4e9e;
    --mark-blue: #1a62b8;
    --shadow: rgba(40, 30, 20, 0.28);
  }
  * { margin: 0; padding: 0; box-sizing: border-box; }
  html, body {
    width: 1200px; height: 1200px; overflow: hidden;
    background: var(--page-bg);
    font-family: "Source Sans 3", "Myriad Pro", sans-serif;
  }
  .canvas { position: relative; width: 1200px; height: 1200px; }
  .card {
    position: absolute; left: 218px; width: 764px; height: 440px;
    background: var(--card-white);
    box-shadow: 0 6px 18px var(--shadow);
    overflow: hidden;
  }
  .card--front { top: 120px; }
  .card--back { top: 640px; }
  .card__band { position: absolute; left: 0; width: 100%; }
  .card__band--top { top: 0; height: 210px; }
  .card__band--bottom { bottom: 0; height: 120px; }

  .contact { position: absolute; left: 0; right: 0; top: 140px; text-align: center; color: var(--ink-blue); }
  .contact__name { font-size: 34px; line-height: 40px; font-weight: 400; }
  .contact__role { font-size: 25px; line-height: 30px; margin-bottom: 24px; }
  .contact__line { font-size: 16px; line-height: 22px; }

  .brand { position: absolute; left: 0; right: 0; top: 70px; text-align: center; }
  .brand__mark {
    display: block; width: 150px; height: 130px; margin: 0 auto 22px;
    background: var(--mark-blue);
  }
  .brand__name {
    color: var(--ink-blue); font-weight: 400;
    font-size: 52px; line-height: 54px; letter-spacing: 2px;
  }
  .brand__name span { display: block; font-size: 22px; line-height: 30px; letter-spacing: 22px; margin-left: 22px; }
  .brand__web {
    position: absolute; left: 0; right: 0; bottom: 44px; text-align: center;
    color: var(--ink-blue); font-size: 24px;
  }
</style>
</head>
<body>
<main class="canvas">
  <section class="card card--front">
    <svg class="card__band card__band--top" viewBox="0 0 764 210" preserveAspectRatio="none" role="img" aria-label="Decorative blue wave band across the top of the card">
      <defs>
        <linearGradient id="topBlue" x1="0" y1="0" x2="0" y2="1">
          <stop offset="0" stop-color="#0b4aa2"/>
          <stop offset="1" stop-color="#2a8ad6"/>
        </linearGradient>
      </defs>
      <path d="M0,0 H764 V205 Q600,110 380,112 Q150,118 0,208 Z" fill="url(#topBlue)"/>
    </svg>
    <div class="contact">
      <h1 class="contact__name">Daniel Harrow</h1>
      <p class="contact__role">president</p>
      <p class="contact__line">418 Kestrel Lane, Leeds, LS9 4QT, UK</p>
      <p class="contact__line">+322 555 014 27</p>
      <p class="contact__line">info@brelvorasystems.com</p>
    </div>
    <svg class="card__band card__band--bottom" viewBox="0 0 764 120" preserveAspectRatio="none" role="img" aria-label="Decorative blue wave band across the bottom of the card">
      <defs>
        <linearGradient id="bottomBlue" x1="0" y1="0" x2="1" y2="0">
          <stop offset="0" stop-color="#2a8ad6"/>
          <stop offset="1" stop-color="#0b4aa2"/>
        </linearGradient>
      </defs>
      <path d="M0,120 Q60,25 250,18 Q400,15 520,45 Q660,65 764,0 V120 Z" fill="url(#bottomBlue)"/>
    </svg>
  </section>

  <section class="card card--back">
    <div class="brand">
      <span class="brand__mark"></span>
      <h2 class="brand__name">BRELVORA<span>SYSTEMS</span></h2>
    </div>
    <p class="brand__web">www.BrelvoraSystems.com</p>
  </section>
</main>
</body>
</html>
```